Bright Lantern Way (BLWY) Business Card - company with a mission

Note* The file attached... orange with "Bright Lantern WAY" (in CAPS) is our logo. I am also open to having the text "bright lantern way" OUTSIDE the orange round logo for business card (so yes, you may take the text out).

The info: (the following info are separate. So either you can use Marcus or Renata for now, but that will be 2 separate cards, not together in one card. Thanks!!

Marcus T Delvin
202.555.0137
marcus@brightlanternway.example
Managing Partner

Renata P Osk
202.555.0184
renata@brightlanternway.example
Managing Partner

Our website: www.brightlanternway.example

BLWY LLC stands for Bright Lantern Way (non profit arm is called lantern glow foundation)—our business is based out of New York City and has a non-profit arm where for every bar of soap you purchase, we donate a bar (don’t want any designs that limits us to only soap). Currently working with South Africa. We want the focus to be organic/natural soap with a mission.

Looking for a clean, fresh design.

Industry/Entity Type

Non-Profit

Requirements
Must have
• Clean, fresh, refreshing. Design should not be too busy.

```html
<!DOCTYPE html>
<html lang="en">
<head>
<meta charset="utf-8">
<title>Bright Lantern Way – Business Card</title>
<link rel="stylesheet" href="https://fonts.googleapis.com/css2?family=Questrial&display=swap">
<style>
  :root {
    --page-bg: #e9e7e4;
    --card-white: #ffffff;
    --brand-orange: #f2ae6c;
    --ink-orange: #e3a15f;
    --mark-white: #ffffff;
    --card-shadow: rgba(0, 0, 0, 0.16);
  }
  * { box-sizing: border-box; margin: 0; padding: 0; }
  html, body {
    width: 1200px;
    height: 900px;
    overflow: hidden;
    background: var(--page-bg);
    font-family: "Questrial", "Century Gothic", sans-serif;
  }
  .sheet {
    width: 1200px;
    height: 900px;
    display: flex;
    flex-direction: column;
    align-items: center;
    justify-content: center;
    gap: 56px;
  }
  .card {
    position: relative;
    width: 620px;
    height: 354px;
    border-radius: 24px;
    box-shadow: 0 10px 28px var(--card-shadow);
    overflow: hidden;
  }
  /* Back side */
  .card--back {
    background: var(--brand-orange);
    display: flex;
    align-items: center;
    justify-content: center;
  }
  .back-mark {
    width: 190px;
    height: 190px;
    border: 9px solid var(--mark-white);
    border-radius: 50%;
    display: flex;
    align-items: center;
    justify-content: center;
  }
  .back-mark__name {
    color: var(--mark-white);
    font-size: 46px;
    letter-spacing: 3px;
  }
  /* Front side */
  .card--front {
    background: var(--card-white);
    color: var(--ink-orange);
  }
  .front-mark {
    position: absolute;
    left: 44px;
    top: 88px;
    width: 118px;
    height: 118px;
    border-radius: 50%;
    background: var(--brand-orange);
    display: flex;
    align-items: center;
    justify-content: center;
  }
  .front-mark__name {
    color: var(--mark-white);
    font-size: 32px;
    letter-spacing: 2px;
  }
  .wordmark {
    position: absolute;
    right: 40px;
    top: 40px;
    font-size: 26px;
    letter-spacing: 1px;
    color: var(--ink-orange);
  }
  .contact {
    position: absolute;
    right: 40px;
    top: 136px;
    text-align: right;
    font-size: 17px;
    line-height: 1.55;
    letter-spacing: 0.5px;
  }
  .person {
    position: absolute;
    left: 48px;
    bottom: 54px;
  }
  .person__name {
    font-size: 27px;
    letter-spacing: 0.5px;
  }
  .person__title {
    font-size: 17px;
    margin-top: 6px;
    letter-spacing: 0.5px;
  }
</style>
</head>
<body>
  <main class="sheet">
    <section class="card card--back" aria-label="Card back">
      <div class="back-mark">
        <span class="back-mark__name">BLWY</span>
      </div>
    </section>

    <section class="card card--front" aria-label="Card front">
      <div class="front-mark">
        <span class="front-mark__name">BLWY</span>
      </div>
      <p class="wordmark">Bright Lantern WAY</p>
      <address class="contact" style="font-style: normal;">
        <div class="contact__phone">202.555.0184</div>
        <div class="contact__email">renata@brightlanternway.example</div>
        <div class="contact__web">www.brightlanternway.example</div>
      </address>
      <div class="person">
        <p class="person__name">Renata P Osk</p>
        <p class="person__title">Managing Partner</p>
      </div>
    </section>
  </main>
</body>
</html>
```